Q9 Clinic business card design

It is a doctor's business card. It will include both English and Chinese information ( will be provided). The design should look professional. It is an obstetrics and gynaecology clinic.

Target Market(s)

Hong Kong private medical market_adult females

Contact Information for Business Card

as the information provided_color coordination with the logo color

Font styles to use
Sans Serif

Colors

Designer to choose colors to be used in the design.

Requirements
Must have
• Logo.
• dr's name, credentials, address, telephone, fax no,

```html
<!DOCTYPE html>
<html lang="en">
<head>
<meta charset="utf-8">
<title>Q9 Clinic business cards</title>
<link href="https://fonts.googleapis.com/css2?family=Lato:wght@400;700&family=Noto+Sans+TC:wght@400;500&display=swap" rel="stylesheet">
<style>
  :root{
    --bg:#2b2b2b;
    --paper:#f7f7f5;
    --blue:#1f7fc4;
    --blue-dark:#1868a8;
    --green:#8cc63f;
    --grey:#8a8f94;
    --white:#ffffff;
  }
  *{box-sizing:border-box;margin:0;padding:0}
  html,body{width:1200px;height:900px;overflow:hidden;background:var(--bg)}
  body{position:relative;font-family:"Lato","Noto Sans TC",sans-serif}
  .card{
    position:absolute;width:540px;height:310px;border-radius:26px;overflow:hidden;
    background:var(--paper);box-shadow:0 18px 40px rgba(0,0,0,.5);
  }
  .card--en{left:70px;top:100px}
  .card--zh{left:590px;top:490px}
  .brand{position:absolute;left:0;right:0;top:46px;text-align:center}
  .brand__name{font-size:28px;font-weight:400;color:var(--blue);letter-spacing:3px}
  .brand__sub{font-size:9px;letter-spacing:2px;color:var(--grey);margin-top:4px}
  .doctor{position:absolute;left:0;right:0;top:118px;text-align:center}
  .doctor__name{font-size:22px;color:var(--blue);font-weight:400}
  .card--zh .doctor{top:112px}
  .card--zh .doctor__name{font-family:"Noto Sans TC",sans-serif;font-size:22px}
  .doctor__creds{font-size:10px;color:var(--green);font-weight:700;margin-top:3px;line-height:1.55}
  .card--zh .doctor__creds{font-family:"Noto Sans TC",sans-serif;font-weight:500;font-size:10px}
  .band-green{position:absolute;left:0;right:0;top:194px;height:28px;background:var(--green);
    display:flex;justify-content:space-between;align-items:center;padding:0 24px;color:var(--white);font-size:12px}
  .band-blue{position:absolute;left:0;right:0;top:222px;bottom:0;
    background:linear-gradient(180deg,var(--blue),var(--blue-dark));
    display:flex;justify-content:space-between;padding:10px 24px;color:var(--white);font-size:11px;line-height:1.5}
  .card--zh .band-blue,.card--zh .band-green{font-family:"Noto Sans TC",sans-serif}
  .contact{display:flex;align-items:center;gap:14px}
  .contact span{display:inline-flex;align-items:center;gap:5px}
  .address{display:flex;gap:6px}
  .address--right{text-align:right}
  svg.icon{width:11px;height:11px;fill:var(--white);flex:none;margin-top:3px}
  .contact svg.icon{margin-top:0}
</style>
</head>
<body>

<section class="card card--en">
  <div class="brand">
    <div class="brand__name">Q9 Clinic</div>
    <div class="brand__sub">OBSTETRICS · GYNAECOLOGY</div>
  </div>
  <div class="doctor">
    <div class="doctor__name">Dr Lam Wai Ming, Vincent</div>
    <div class="doctor__creds">MBBS, MD, FCOG, FAGS, FWOG</div>
  </div>
  <div class="band-green">
    <div class="contact">
      <span><svg class="icon" viewBox="0 0 24 24"><path d="M6.6 10.8a15 15 0 0 0 6.6 6.6l2.2-2.2a1 1 0 0 1 1-.25 11 11 0 0 0 3.6.6 1 1 0 0 1 1 1V20a1 1 0 0 1-1 1A17 17 0 0 1 3 4a1 1 0 0 1 1-1h3.5a1 1 0 0 1 1 1 11 11 0 0 0 .6 3.6 1 1 0 0 1-.25 1z"/></svg>000 000 0000</span>
      <span><svg class="icon" viewBox="0 0 24 24"><path d="M6 3h10v5H6zM3 9h18v9h-3v3H6v-3H3zm5 7v3h8v-3z"/></svg>000 000 0000</span>
    </div>
    <div>Messaging booking no. XXXXXX</div>
  </div>
  <div class="band-blue">
    <div class="address">
      <svg class="icon" viewBox="0 0 24 24"><path d="M12 2a7 7 0 0 0-7 7c0 5 7 13 7 13s7-8 7-13a7 7 0 0 0-7-7zm0 9.5A2.5 2.5 0 1 1 12 6.5a2.5 2.5 0 0 1 0 5z"/></svg>
      <div>Unit 1205, 12th floor, Harbourlight Plaza<br>6 Kwan Lok Street, Fo Tan, Shatin<br>New Territories, HONG KONG</div>
    </div>
    <div class="address address--right">
      <div>Unit 1710, 17th floor, Tower B, Lumen Place<br>58 Canton Road, Tsimshatsui<br>Kowloon, HONG KONG</div>
      <svg class="icon" viewBox="0 0 24 24"><path d="M12 2a7 7 0 0 0-7 7c0 5 7 13 7 13s7-8 7-13a7 7 0 0 0-7-7zm0 9.5A2.5 2.5 0 1 1 12 6.5a2.5 2.5 0 0 1 0 5z"/></svg>
    </div>
  </div>
</section>

<section class="card card--zh" lang="zh-Hant">
  <div class="brand">
    <div class="brand__name">Q9 Clinic</div>
    <div class="brand__sub">OBSTETRICS · GYNAECOLOGY</div>
  </div>
  <div class="doctor">
    <div class="doctor__name">林偉明醫生</div>
    <div class="doctor__creds">內外全科醫學士　醫學博士　婦產科專科醫生<br>婦產科學會會員　婦科醫學會會員</div>
  </div>
  <div class="band-green">
    <div class="contact">
      <span><svg class="icon" viewBox="0 0 24 24"><path d="M6.6 10.8a15 15 0 0 0 6.6 6.6l2.2-2.2a1 1 0 0 1 1-.25 11 11 0 0 0 3.6.6 1 1 0 0 1 1 1V20a1 1 0 0 1-1 1A17 17 0 0 1 3 4a1 1 0 0 1 1-1h3.5a1 1 0 0 1 1 1 11 11 0 0 0 .6 3.6 1 1 0 0 1-.25 1z"/></svg>000 000 0000</span>
      <span><svg class="icon" viewBox="0 0 24 24"><path d="M6 3h10v5H6zM3 9h18v9h-3v3H6v-3H3zm5 7v3h8v-3z"/></svg>000 000 0000</span>
    </div>
    <div>預約電話號碼</div>
  </div>
  <div class="band-blue">
    <div class="address">
      <svg class="icon" viewBox="0 0 24 24"><path d="M12 2a7 7 0 0 0-7 7c0 5 7 13 7 13s7-8 7-13a7 7 0 0 0-7-7zm0 9.5A2.5 2.5 0 1 1 12 6.5a2.5 2.5 0 0 1 0 5z"/></svg>
      <div>沙田火炭群樂街6號港灣廣場12樓<br>1205室</div>
    </div>
    <div class="address address--right">
      <div>尖沙咀廣東道58號朗晴廣場B座17<br>樓1710室</div>
      <svg class="icon" viewBox="0 0 24 24"><path d="M12 2a7 7 0 0 0-7 7c0 5 7 13 7 13s7-8 7-13a7 7 0 0 0-7-7zm0 9.5A2.5 2.5 0 1 1 12 6.5a2.5 2.5 0 0 1 0 5z"/></svg>
    </div>
  </div>
</section>

</body>
</html>
```